New Personal Trainer needs poster to attract clients

Hi I am a personal trainer working inside a busy gym. My sole base of clients is from the gym itself where I compete with other trainers for business.
New company so my brand is still not noticed by the public.
My company name is Stridewell PT.
I am looking for a poster that will attract attention and increase awareness of my brand. My market will be mostly overweight men/women aged from 25-55 years old.
I would like pics of some sort on there that would be appropriate for my target market. Design needs to be colorful to attract attention.

My name and number must be added as well as facebook details
Dean Harlow
0437290518
(Facebook Symbol) Dean Harlow PT

Target Market(s)

Overweight men and women aged 25-55 years. Some would be mothers with young children

Industry/Entity Type

Fitness

Font styles to use
Sans Serif

Requirements
Must have
• My Logo.
• Pictures.
• Bright Attractive colours
• My name and number
• Slogan
Nice to have
• Slogan I'm leaning towards is "Building a Better You" but open to any ideas with this.

```html
<!DOCTYPE html>
<html lang="en">
<head>
<meta charset="utf-8">
<title>Stridewell PT Poster</title>
<link href="https://fonts.googleapis.com/css2?family=Titillium+Web:ital,wght@0,700;0,900;1,700;1,900&display=swap" rel="stylesheet">
<style>
  :root {
    --backdrop: #4f9bc8;
    --paper: #ffffff;
    --brand-blue: #0a7ec8;
    --band-blue: #1f8fd6;
    --brand-yellow: #fde02a;
    --ink: #1f1f24;
    --rule: #6b6b70;
    --photo-warm: #c9a48a;
    --photo-cool: #6f7c88;
  }
  * { margin: 0; padding: 0; box-sizing: border-box; }
  html, body { width: 1200px; height: 705px; overflow: hidden; }
  body {
    background: var(--backdrop);
    font-family: "Titillium Web", Arial, sans-serif;
    position: relative;
  }
  .poster {
    position: absolute;
    left: 357px;
    top: 0;
    width: 486px;
    height: 687px;
    background: var(--paper);
    transform: translate(0, 9px);
    overflow: hidden;
  }
  .brand-name {
    position: absolute;
    left: 38px;
    top: 48px;
    width: 412px;
    font-weight: 900;
    font-size: 59px;
    line-height: 1;
    color: var(--brand-blue);
    letter-spacing: 0.5px;
    white-space: nowrap;
  }
  .brand-rule {
    position: absolute;
    left: 38px;
    top: 140px;
    width: 410px;
    height: 2px;
    background: var(--brand-blue);
  }
  .slogan-band {
    position: absolute;
    left: 0; top: 201px;
  }
  .slogan-text {
    position: absolute;
    left: 40px; top: 201px;
    width: 404px; height: 19px;
    line-height: 19px;
    text-align: center;
    color: var(--paper);
    font-style: italic;
    font-weight: 700;
    font-size: 11px;
    letter-spacing: 7px;
  }
  .photo-strip {
    position: absolute;
    left: 0; top: 231px;
  }
  .contact-band {
    position: absolute;
    left: 0; top: 474px;
  }
  .trainer-name {
    position: absolute;
    left: 62px; top: 474px;
    color: var(--paper);
    font-style: italic;
    font-weight: 900;
    font-size: 33px;
    line-height: 1.1;
    white-space: nowrap;
  }
  .trainer-phone {
    position: absolute;
    left: 64px; top: 512px;
    color: var(--paper);
    font-style: italic;
    font-weight: 700;
    font-size: 17px;
    line-height: 1;
    white-space: nowrap;
  }
  .trainer-social {
    position: absolute;
    left: 64px; top: 537px;
    display: flex;
    align-items: center;
    gap: 5px;
    color: var(--paper);
    font-style: italic;
    font-weight: 700;
    font-size: 13px;
    line-height: 1;
    white-space: nowrap;
  }
  .social-dot {
    width: 14px; height: 14px;
    border-radius: 50%;
    background: var(--paper);
  }
  .offer {
    position: absolute;
    left: 366px; top: 480px;
    color: var(--ink);
    font-style: italic;
    font-weight: 700;
  }
  .offer-title { font-size: 11px; line-height: 1; margin-bottom: 6px; }
  .offer-list { list-style: none; font-size: 9px; line-height: 13.5px; }
  .offer-list li::before { content: "•"; margin-right: 6px; }
  .double-rule {
    position: absolute;
    left: 38px; top: 599px;
    width: 410px; height: 4px;
    border-top: 1px solid var(--rule);
    border-bottom: 1px solid var(--rule);
  }
  .tagline {
    position: absolute;
    left: 38px; top: 618px;
    width: 416px;
    color: var(--ink);
    font-style: italic;
    font-weight: 900;
    font-size: 21.5px;
    line-height: 1.2;
    white-space: nowrap;
  }
</style>
</head>
<body>
  <main class="poster">
    <div class="brand-name">STRIDEWELL PT</div>
    <div class="brand-rule"></div>

    <svg class="slogan-band" width="486" height="30" viewBox="0 0 486 30" aria-hidden="true">
      <polygon points="46,0 444,0 438,19 40,19" fill="var(--band-blue)"/>
    </svg>
    <div class="slogan-text">BUILDING A BETTER YOU</div>

    <svg class="photo-strip" width="486" height="225" viewBox="0 0 486 225">
      <defs>
        <linearGradient id="photo-one" x1="0" y1="0" x2="1" y2="1">
          <stop offset="0" stop-color="#8b9196"/>
          <stop offset="0.6" stop-color="#c98e9a"/>
          <stop offset="1" stop-color="#3b4150"/>
        </linearGradient>
        <linearGradient id="photo-two" x1="0" y1="0" x2="1" y2="0">
          <stop offset="0" stop-color="#2a2a2e"/>
          <stop offset="0.5" stop-color="#c46a3a"/>
          <stop offset="1" stop-color="#cfc6c0"/>
        </linearGradient>
        <linearGradient id="photo-three" x1="0" y1="0" x2="0" y2="1">
          <stop offset="0" stop-color="#d8dde2"/>
          <stop offset="1" stop-color="#5e6670"/>
        </linearGradient>
      </defs>
      <polygon role="img" aria-label="Photo: woman training on a bench press in the gym" points="0,0 130,0 65,225 0,225" fill="url(#photo-one)"/>
      <polygon role="img" aria-label="Photo: trainer coaching a woman on suspension straps" points="137,0 413,0 348,225 72,225" fill="url(#photo-two)"/>
      <polygon role="img" aria-label="Photo: fit woman standing in workout clothes" points="420,0 486,0 486,225 355,225" fill="url(#photo-three)"/>
    </svg>

    <svg class="contact-band" width="486" height="90" viewBox="0 0 486 90" aria-hidden="true">
      <rect x="0" y="0" width="486" height="90" fill="var(--brand-yellow)"/>
      <polygon points="50,0 338,0 313,90 26,90" fill="var(--band-blue)"/>
    </svg>
    <div class="trainer-name">DEAN HARLOW</div>
    <div class="trainer-phone">CALL US : 0437290518</div>
    <div class="trainer-social"><span class="social-dot"></span>DEAN HARLOW PT</div>

    <div class="offer">
      <div class="offer-title">WHAT WE OFFER</div>
      <ul class="offer-list">
        <li>WEIGH TRAINING</li>
        <li>DIET NUTRITION</li>
        <li>TIME MANAGEMENET</li>
        <li>PERSONAL TRAINING</li>
      </ul>
    </div>

    <div class="double-rule"></div>
    <div class="tagline">HEALTHY LIVING STARTS WITH WORK OUT</div>
  </main>
</body>
</html>
```